KVD INDUSTRIES TOMB CARD DESIGN

KVD Industries
Prineville Office: 2284 SW Hollister Rd, Prineville, OR 97754
Redmond Office: 4718 NW 47th Street, Redmond, OR 97756
Serving continuous Process Industries Since 1981
Manufacturing, Welding, machining, Design, Reverse Engineering

Welding

Contact Information for Business Card

Tom Bristow
CEO/TECHNICAL ANALYST
Phone: 1-541-555-0142
DIRECT LINE: 1-541-555-0187
Cell No 1-541-555-0163

```html
<!DOCTYPE html>
<html lang="en">
<head>
<meta charset="utf-8">
<title>KVD Industries – Business Card</title>
<link rel="stylesheet" href="https://fonts.googleapis.com/css2?family=Oswald:wght@500;700&family=Montserrat:wght@500;600&display=swap">
<style>
  :root {
    --ink-indigo: #34367f;
    --band-top: #3b3d86;
    --band-mid: #7b7db3;
    --band-bottom: #d9dae9;
    --card-white: #ffffff;
    --backdrop: #ecebe8;
    --text-dark: #111114;
  }
  * { box-sizing: border-box; margin: 0; padding: 0; }
  html, body { width: 1200px; height: 902px; overflow: hidden; }
  body { background: var(--backdrop); position: relative; }

  .business-card {
    position: absolute; left: 100px; top: 165px;
    width: 1000px; height: 572px;
    background: var(--card-white);
    border-radius: 6px;
    box-shadow: 0 10px 30px rgba(0,0,0,.12);
    overflow: hidden;
  }
  .accent-band {
    position: absolute; left: 600px; top: 0; right: 0; bottom: 0;
    background: linear-gradient(180deg, var(--band-top) 0%, var(--band-mid) 45%, var(--band-bottom) 100%);
    border-top-left-radius: 40px;
  }

  .brand-mark {
    position: absolute; left: 70px; top: 80px;
    display: flex; align-items: center; gap: 18px;
  }
  .brand-mark__square { width: 42px; height: 42px; background: var(--ink-indigo); }
  .brand-mark__name {
    font-family: "Oswald", sans-serif; font-weight: 700;
    font-size: 46px; letter-spacing: 1px; color: var(--ink-indigo);
  }

  .info-panel {
    position: absolute; left: 470px; top: 95px;
    width: 480px; height: 390px;
    background: var(--card-white);
    padding: 40px 36px;
  }
  .company-name {
    font-family: "Oswald", sans-serif; font-weight: 700;
    font-size: 52px; line-height: 1; color: var(--text-dark); letter-spacing: .5px;
  }
  .tagline {
    margin-top: 8px;
    font-family: "Oswald", sans-serif; font-weight: 500;
    font-size: 15px; letter-spacing: .6px; color: var(--ink-indigo);
    text-transform: uppercase;
  }
  .details { list-style: none; margin-top: 38px; }
  .details__item {
    position: relative; padding-left: 28px; margin-bottom: 20px;
    font-family: "Montserrat", sans-serif; font-weight: 500;
    font-size: 17px; line-height: 1.45; color: var(--ink-indigo);
    text-transform: uppercase;
  }
  .details__item::before {
    content: ""; position: absolute; left: 0; top: 6px;
    width: 13px; height: 13px; border-radius: 50%; background: var(--ink-indigo);
  }
</style>
</head>
<body>
  <article class="business-card">
    <div class="accent-band"></div>

    <div class="brand-mark">
      <span class="brand-mark__square"></span>
      <span class="brand-mark__name">KVD INDUSTRIES</span>
    </div>

    <section class="info-panel">
      <h1 class="company-name">KVD INDUSTRIES</h1>
      <p class="tagline">Serving Continuous Process Industries Since 1981</p>
      <ul class="details">
        <li class="details__item">Tom Bristow<br>CEO/Technical Analyst</li>
        <li class="details__item">Contact:<br>Phone: 1-541-555-0142<br>Direct Line: 1-541-555-0187<br>Cell No: 1-541-555-0163</li>
      </ul>
    </section>
  </article>
</body>
</html>
```